Brindle Gateworks garage door installation service and repairs

I need a business card design for my company that is called Brindle Gateworks, I install, service, repair and automate garaged doors.
I want my card to look simple and neat but I also want the information such as contact number, email address and website to be clear and noticeable. I would love a simple logo if possible, I would like to see the color blue in the card but not overpowering.

Industry/Entity Type

Garage

```html
<!DOCTYPE html>
<html lang="en">
<head>
<meta charset="utf-8">
<title>Brindle Gateworks – Business Card</title>
<link rel="stylesheet" href="https://fonts.googleapis.com/css2?family=Oswald:wght@400;500;600&display=swap">
<style>
  :root {
    --page-bg: #e9e6e1;
    --card-white: #ffffff;
    --blue-deep: #0a0f8c;
    --blue-mid: #1a1fd6;
    --blue-bright: #2a35ff;
    --brand-blue: #1c22f0;
    --ink: #1b1b1b;
    --rule-grey: #8a8a8a;
    --text-light: #ffffff;
  }
  * { margin: 0; padding: 0; box-sizing: border-box; }
  html, body {
    width: 1200px; height: 1000px; overflow: hidden;
    background: var(--page-bg);
  }
  .business-card {
    position: absolute;
    left: 78px; top: 202px;
    width: 1044px; height: 596px;
    background: var(--card-white);
    overflow: hidden;
    box-shadow: 0 6px 18px rgba(0,0,0,0.25);
    font-family: "Oswald", sans-serif;
  }
  .blue-band { position: absolute; inset: 0; width: 1044px; height: 596px; }
  .holder-name {
    position: absolute; right: 38px; top: 44px;
    color: var(--text-light);
    font-size: 50px; font-weight: 500;
    font-variant: small-caps; letter-spacing: 1px;
    text-shadow: 2px 3px 3px rgba(0,0,0,0.45);
  }
  .contact-list {
    position: absolute; right: 36px; top: 176px;
    list-style: none; text-align: right;
  }
  .contact-item {
    display: flex; justify-content: flex-end; align-items: center;
    gap: 14px; height: 46px;
    color: var(--text-light);
    font-size: 35px; font-weight: 400; letter-spacing: 1.5px;
    text-shadow: 2px 3px 3px rgba(0,0,0,0.45);
  }
  .contact-icon { width: 30px; height: 30px; flex: none; }
  .brand-lockup {
    position: absolute; left: 100px; top: 358px;
    display: flex; align-items: center; gap: 22px;
  }
  .brand-square { width: 104px; height: 104px; background: var(--brand-blue); }
  .brand-name {
    color: var(--brand-blue);
    font-size: 72px; font-weight: 600; line-height: 1;
    letter-spacing: 1px;
  }
  .service-rule {
    position: absolute; left: 48px; top: 528px;
    width: 702px; height: 4px; background: var(--rule-grey);
  }
  .service-line {
    position: absolute; left: 52px; top: 534px;
    color: var(--ink);
    font-size: 19px; font-weight: 500; letter-spacing: 3px;
    white-space: nowrap;
  }
</style>
</head>
<body>
  <section class="business-card">
    <svg class="blue-band" viewBox="0 0 1044 596" aria-hidden="true">
      <defs>
        <linearGradient id="bandGradient" x1="0" y1="0" x2="1" y2="0.6">
          <stop offset="0" stop-color="var(--blue-deep)"/>
          <stop offset="0.45" stop-color="var(--blue-mid)"/>
          <stop offset="1" stop-color="var(--blue-bright)"/>
        </linearGradient>
      </defs>
      <polygon points="0,0 1044,0 1044,336 392,336 0,93" fill="url(#bandGradient)"/>
    </svg>

    <h1 class="holder-name">Dale Merrick</h1>

    <ul class="contact-list">
      <li class="contact-item">0412-867-305
        <svg class="contact-icon" viewBox="0 0 30 30" aria-label="phone">
          <rect x="8" y="3" width="14" height="24" rx="2" fill="none" stroke="#fff" stroke-width="2"/>
          <line x1="13" y1="23" x2="17" y2="23" stroke="#fff" stroke-width="2"/>
        </svg>
      </li>
      <li class="contact-item">dale@brindlegate.com.au
        <svg class="contact-icon" viewBox="0 0 30 30" aria-label="email">
          <rect x="2" y="7" width="26" height="17" fill="#fff"/>
          <polyline points="2,7 15,17 28,7" fill="none" stroke="#1a1fd6" stroke-width="1.5"/>
        </svg>
      </li>
      <li class="contact-item">brindlegate.com.au
        <svg class="contact-icon" viewBox="0 0 30 30" aria-label="website">
          <circle cx="15" cy="15" r="12" fill="none" stroke="#fff" stroke-width="1.8"/>
          <ellipse cx="15" cy="15" rx="5" ry="12" fill="none" stroke="#fff" stroke-width="1.5"/>
          <line x1="3" y1="15" x2="27" y2="15" stroke="#fff" stroke-width="1.5"/>
          <line x1="5" y1="9" x2="25" y2="9" stroke="#fff" stroke-width="1.2"/>
          <line x1="5" y1="21" x2="25" y2="21" stroke="#fff" stroke-width="1.2"/>
        </svg>
      </li>
    </ul>

    <div class="brand-lockup">
      <div class="brand-square" aria-hidden="true"></div>
      <p class="brand-name">Brindle Gateworks</p>
    </div>

    <div class="service-rule" aria-hidden="true"></div>
    <p class="service-line">INSTALL | SERVICE | REPAIR | AUTOMATE | REMOTES</p>
  </section>
</body>
</html>
```